Webdesign für Hausmeisterservice, Garten- und Landschaftsbau
Zielgruppe
Hausmeisterservice und Garten und Landschaftsbau
Aufgabenstellung
habe schon eine Webseite erstellt die muss Designt werden. Wohnpfleger.info

```html
<!DOCTYPE html>
<html lang="de">
<head>
<meta charset="utf-8">
<title>Wohnpfleger – Hausmeister Service</title>
<link rel="stylesheet" href="https://fonts.googleapis.com/css2?family=Open+Sans:wght@700;800&family=Lato:wght@400;700&display=swap">
<style>
:root{
  --grey:#ebebeb;
  --red:#a8423f;
  --cyan:#0b86bf;
  --blue:#0a5ea8;
  --footer:#035ca6;
  --ink:#2a2a2a;
  --white:#ffffff;
}
*{margin:0;padding:0;box-sizing:border-box}
html,body{width:1200px;height:2218px;overflow:hidden;background:var(--white)}
body{position:relative;font-family:"Lato",sans-serif;color:var(--ink)}
.abs{position:absolute}
.hero{left:0;top:0;width:1200px;height:675px;background:var(--grey)}
.hero-art{left:0;top:0}
.hero-kicker{left:300px;top:52px;font-family:"Open Sans",sans-serif;font-weight:700;font-size:29px;line-height:41px;color:var(--red)}
.brand{left:69px;top:262px;display:flex;align-items:center;gap:10px}
.brand-mark{width:26px;height:26px;background:var(--blue)}
.brand-name{font-family:"Open Sans",sans-serif;font-weight:800;font-size:32px;color:var(--blue)}
.hero-title{left:69px;top:382px;font-family:"Open Sans",sans-serif;font-weight:700;font-size:41px;line-height:48px;color:var(--cyan)}
.intro{left:342px;top:733px;width:530px;font-size:13px;line-height:20.6px}
.intro p+p{margin-top:20.6px}
.intro-cta{left:342px;top:914px;width:540px;font-family:"Open Sans",sans-serif;font-weight:700;font-size:24px;line-height:33px;color:var(--blue)}
.keeping-art{left:0;top:1050px}
.service-heads{left:350px;top:1052px;font-family:"Open Sans",sans-serif;font-weight:700;font-size:36px;line-height:62px;color:var(--ink)}
.service-heads .accent{color:var(--blue)}
.tasks{left:734px;top:1060px;width:370px;font-size:13px;line-height:20.6px}
.tasks h3{font-weight:400;font-size:13px;color:var(--blue);padding-left:15px}
.tasks ul{list-style:none;margin-bottom:27px}
.tasks li{position:relative;padding-left:15px}
.tasks li::before{content:"";position:absolute;left:0;top:8px;width:5px;height:5px;border-radius:50%;background:var(--ink)}
.footer{left:0;top:1812px;width:1200px;height:406px;background:var(--footer);color:var(--white)}
.footer-title{left:95px;top:55px;font-family:"Open Sans",sans-serif;font-weight:700;font-size:24px}
.footer-contact{left:95px;top:105px;font-size:34px;line-height:49px}
.footer-legal{left:95px;top:228px;font-size:21px;line-height:33px}
.footer-address{left:605px;top:103px;font-size:21px;line-height:33px}
.footer-links{left:605px;top:228px;font-size:21px;line-height:33px}
</style>
</head>
<body>
<section class="hero abs">
  <svg class="hero-art abs" width="1200" height="675" viewBox="0 0 1200 675">
    <defs>
      <linearGradient id="fold" x1="0" y1="0" x2="1" y2="0">
        <stop offset="0" stop-color="#d4d4d4"/>
        <stop offset="1" stop-color="#ebebeb"/>
      </linearGradient>
      <linearGradient id="tools" x1="0" y1="0" x2="1" y2="1">
        <stop offset="0" stop-color="#3a4fa8"/>
        <stop offset="0.55" stop-color="#2437a0"/>
        <stop offset="1" stop-color="#9b2b38"/>
      </linearGradient>
    </defs>
    <polygon points="176,0 200,0 455,344 439,344" fill="url(#fold)"/>
    <polygon points="758,0 1200,0 1200,675 685,675 439,344" fill="url(#tools)" role="img" aria-label="Foto: Schraubenschlüssel und Schraubendreher in der Tasche einer blauen Arbeitshose vor kariertem Hemd"/>
  </svg>
  <div class="hero-kicker abs">GARTEN &amp;<br>LANDSCHAFTSBAU</div>
  <div class="brand abs"><span class="brand-mark"></span><span class="brand-name">Wohnpfleger</span></div>
  <h1 class="hero-title abs">HAUSMEISTER<br>SERVICE</h1>
</section>

<section class="intro abs">
  <p>Als Hausmeisterservice fühlen wir uns für das gesamte übertragene Objekt verantwortlich. Innen erledigen wir kleine Reparaturen, überwachen die Heizungsanlage und führen bei Bedarf auch Entrümpelungen von Kellern und Wohnungen durch.</p>
  <p>Nach der Entrümpelung renovieren wir die Räume schnell und fachgerecht, sodass sie wieder genutzt werden können. Außen kümmern wir uns um die Zuwegungen, erledigen die Gartenarbeiten ganzjährig und unser Winterdienst sorgt bei Schnee und Glätte für freie und gesicherte Wege.</p>
</section>
<h2 class="intro-cta abs">WIR FREUEN UNS AUF IHRE ANFRAGE UND IHREN AUFTRAG.</h2>

<svg class="keeping-art abs" width="730" height="597" viewBox="0 0 730 597">
  <defs>
    <linearGradient id="clean" x1="0" y1="0" x2="1" y2="1">
      <stop offset="0" stop-color="#47586a"/>
      <stop offset="0.45" stop-color="#c9a63a"/>
      <stop offset="1" stop-color="#eef0f2"/>
    </linearGradient>
  </defs>
  <path d="M0,0 H180 Q192,0 200,9 L723,597 H0 Z" fill="url(#clean)" role="img" aria-label="Foto: Reinigungskraft mit gelben Handschuhen, Sprühflasche und Tuch an einem Waschbecken"/>
</svg>

<div class="service-heads abs">
  <div class="accent">HOUSEKEEPING</div>
  <div>PARTNERSCHAFT</div>
  <div>24H SERVICE</div>
</div>

<section class="tasks abs">
  <h3>Wohn-, Schlafzimmer &amp; Kinderzimmer:</h3>
  <ul>
    <li>Alle zugänglichen Oberflächen sowie die Außenseite der Schränke und Kommoden abwischen</li>
    <li>Spiegel und Glasflächen abwischen</li>
    <li>Den Boden reinigen</li>
    <li>Mülleimer leeren und Müllbeutel ersetzen</li>
  </ul>
  <h3>Küche</h3>
  <ul>
    <li>Dreckiges Geschirr in den Geschirrspüler einräumen und einschalten</li>
    <li>Alle zugänglichen Oberflächen, Fliesen sowie die Außenseite des Ofens, der Schränke, des Kühlschranks und der Dunstabzugshaube reinigen</li>
    <li>Den Boden reinigen</li>
    <li>Armaturen und Waschbecken reinigen</li>
    <li>Mülleimer leeren und Mülbeutel ersetzen</li>
  </ul>
  <h3>Badezimmer</h3>
  <ul>
    <li>Alle zugänglichen Oberflächen sowie die Außenseite der Schränke und Kommoden abwischen</li>
    <li>Spiegel und Glasflächen abwischen</li>
    <li>Armaturen, Waschbecken, Duschkabine / Badewanne, einschließlich des Spritzwasserbereich reinigen</li>
    <li>Den Boden reinigen</li>
    <li>Mülleimer leeren und Mülbeutel ersetzen</li>
  </ul>
</section>

<footer class="footer abs">
  <h2 class="footer-title abs">WIR FREUEN UNS VON IHNEN ZU HÖREN</h2>
  <div class="footer-contact abs">0176 - 555 210 47<br>kontakt@wohnpfleger.info</div>
  <div class="footer-legal abs">©2023 Jonas Brandt<br>Impressum<br>Datenschutzerklärung</div>
  <div class="footer-address abs">Jonas Brandt<br>Lindenallee 14<br>Musterstadt 52000</div>
  <div class="footer-links abs">Garten &amp; Landschaftsbau<br>Hausmeister Service</div>
</footer>
</body>
</html>
```